Small Local Computer Shop Website Needed

Im after a new website that goes with my brand logo.
We are a small all family run local computer repair company and would like to drive more business via the site.
I have added my old site and one that was in progress also a Facebook link to give you an idea.

I would like to be able to make it stand out more and be easy to navigate.
I am basically a small computer repair shop, we offer in store repairs and upgrades. We also do call outs to your home or business and we also sell laptops,pcs and peripherals.

We do sell Laptops and pcs and although i don't really want to sell directly from the web it would be nice to be able to show what we have on offer on our site, Roughly 20-30 items generally.

Current site
http://bytevanrepair.com

New Site
http://bytevanrepair.com/site/

Facebook
http://www.facebook.com/pages/Byte-Van/584120937716204

images and files are available.

Many Thanks
Colin
Byte Van

Target Market(s)

I cater for all ages!

Industry/Entity Type

It Company

Number of Pages Required

5+ page

Font styles to use
Sans Serif

Requirements
Must have
• Be nice to keep in theme with my Logo.
• Landing page.
• Contact page
• about us
• Laptops (Displaying products currently for sale in store) Generally 10-20 at a time
• Pcs (Displaying products currently for sale in store)
Nice to have
• i would like and easy way for the customers to navigate to my remote support site. ie.
• https://www.quickhelpdesk.com/
• Easy link to download there trial off shieldmark antivirus.
• ie http://downloads.shieldmark.com/partners/rskit/ShieldMarkDownloader_bytevankit.exe
• Link to our Repair tracker... When we check in a computer or laptop repair the Customers can see how there jobs progressing by clicking the link. ie http://bytevanrepair.com/shop/repairstatus/
• would be great if there was a fairly straight forward way to add/ remove pc's and laptops for sale on our site.
• Maybe check our facebook for ideas images etc..
• https://www.facebook.com/Byte-van-584120937716204/
Should not have
• The site i currently have i really dislike, so please dont copy that theme.
• Had a few designs with a white banner at the top with my logo.
• Sorry but have decided these are not what i want.
• a darker theme is def more in line with what im looking for.
• Thanks

```html
<!DOCTYPE html>
<html lang="en">
<head>
<meta charset="utf-8">
<title>Byte Van – Computer Repair</title>
<link rel="stylesheet" href="https://fonts.googleapis.com/css2?family=Raleway:wght@400;500;600;700&display=swap">
<style>
:root{
  --navy:#0d3556;
  --navy-deep:#0a2a46;
  --blue:#1a6ea3;
  --blue-dark:#13557f;
  --hero-light:#2f78a6;
  --hero-dark:#0f3b5c;
  --yellow:#f2d935;
  --yellow-dark:#d9bf1c;
  --yellow-line:#b79f12;
  --ink:#2b3540;
  --paper:#ffffff;
  --strip:#d7dfe4;
  --sky:#d9eef8;
  --grey:#8a96a0;
}
*{box-sizing:border-box;margin:0;padding:0}
html,body{width:1200px;height:2483px;overflow:hidden}
body{font-family:'Raleway',sans-serif;color:var(--ink);background:var(--navy);position:relative}
.abs{position:absolute}

/* header */
.site-header{left:0;top:0;width:1200px;height:105px;background:linear-gradient(var(--navy-deep),var(--navy))}
.brand{left:165px;top:26px;display:flex;align-items:center;gap:12px;color:#fff;font-weight:700;font-size:40px;letter-spacing:1px}
.brand-dot{width:22px;height:22px;border-radius:50%;background:var(--yellow)}
.service-box{left:723px;top:14px;width:414px;height:77px;background:#e4e8eb;border-radius:6px;display:flex;padding:10px 22px;gap:40px}
.service-box h4{color:var(--blue);font-size:17px;font-weight:600}
.service-box p{font-size:16px;color:var(--ink);margin-top:8px;display:flex;align-items:center;gap:8px}
.service-box p svg{flex:none}

/* nav */
.main-nav{left:0;top:105px;width:1200px;height:75px;background:linear-gradient(var(--yellow),var(--yellow-dark));border-bottom:2px solid var(--yellow-line)}
.main-nav ul{list-style:none;position:absolute;left:179px;top:0;display:flex;height:75px}
.main-nav li{height:75px;display:flex;align-items:center;justify-content:center;border-left:1px solid var(--yellow-line);font-size:17px;color:var(--ink)}
.main-nav li:last-child{border-right:1px solid var(--yellow-line)}

/* hero */
.hero{left:0;top:180px;width:1200px;height:1097px;background:radial-gradient(ellipse at 50% 35%,var(--hero-light),var(--hero-dark) 80%)}
.slider{left:152px;top:8px;width:896px;height:392px;background:var(--paper);box-shadow:0 6px 18px rgba(0,0,0,.35)}
.slider-photo{left:400px;top:0;width:496px;height:392px;background:linear-gradient(160deg,#f4f5f6,#c8cdd1 60%,#8d949b)}
.slider-title{left:14px;top:148px;font-size:29px;color:var(--ink)}
.slider-title strong{color:var(--blue);font-weight:700}
.btn{display:inline-flex;align-items:center;justify-content:center;border-radius:8px;font-weight:600}
.btn-read{left:126px;top:236px;width:118px;height:38px;background:var(--blue-dark);color:#fff;font-size:15px}
.arrow{top:160px;width:30px;height:40px;background:var(--yellow);border-radius:50%;display:flex;align-items:center;justify-content:center}

.features{left:199px;top:380px;width:794px;height:185px;display:flex;box-shadow:0 4px 12px rgba(0,0,0,.3)}
.feature{flex:1;background:linear-gradient(var(--yellow),#e8ca1f);border-right:1px solid var(--yellow-line);padding:14px 18px;text-align:center}
.feature:last-child{border-right:none}
.feature h3{color:var(--blue);font-size:17px;font-weight:600;margin:8px 0 10px}
.feature p{font-size:10.5px;line-height:1.65;color:var(--ink)}

.welcome{left:367px;top:584px;width:439px;height:105px;background:var(--blue-dark);border:5px solid #0f4466;display:flex;flex-direction:column;align-items:center;justify-content:center;color:#fff;font-size:25px;font-weight:400;letter-spacing:1.5px;box-shadow:0 4px 10px rgba(0,0,0,.35)}
.welcome::after{content:"";width:70px;height:3px;background:var(--yellow);margin-top:10px}

.about{left:152px;top:758px;width:524px;color:#e6eef4;font-size:14px;line-height:1.75}
.about p{margin-bottom:18px}
.van-photo{left:690px;top:772px;width:358px;height:234px;border-radius:40% 40% 20% 20%;background:linear-gradient(#e2e6ea,#9aa4ad)}

/* brand strip */
.brands{left:0;top:1277px;width:1200px;height:199px;background:var(--strip)}
.brand-name{top:84px;font-size:26px;font-weight:600;color:#56626c;transform:translateX(-50%)}

/* experts */
.experts{left:0;top:1476px;width:1200px;height:395px;background:linear-gradient(120deg,#d4dc6a,#a3bf4c 45%,#5f8a3c)}
.experts-box{left:270px;top:102px;width:773px;height:105px;background:rgba(255,255,255,.8);border-radius:6px;display:flex;align-items:center;justify-content:center;font-size:30px;font-weight:400;color:var(--blue);letter-spacing:1px}
.btn-market{left:452px;top:268px;width:176px;height:46px;background:var(--blue);color:#fff;font-size:16px;font-weight:500}
.btn-services{left:685px;top:268px;width:176px;height:46px;background:var(--yellow);color:var(--ink);font-size:16px;font-weight:500}

/* testimonials */
.testimonials{left:0;top:1871px;width:1200px;height:419px;background:var(--sky)}
.testi-heading{left:152px;top:22px;font-size:24px;font-weight:500;letter-spacing:1px;color:var(--ink);border-bottom:2px solid var(--blue);padding-bottom:2px}
.testi-heading span{color:var(--blue);font-weight:400}
.quote{top:93px;width:264px;height:111px;background:#fff;border:1px solid #b6c8d2;padding:14px 28px;font-size:12px;line-height:1.6}
.quote::after{content:"";position:absolute;left:50%;bottom:-12px;width:20px;height:20px;background:#fff;border-right:1px solid #b6c8d2;border-bottom:1px solid #b6c8d2;transform:translateX(-50%) rotate(45deg)}
.quote .mark{position:absolute;color:var(--blue);font-size:30px;font-weight:700;line-height:1}
.portrait{top:240px;width:118px;height:118px;border-radius:50%;background:radial-gradient(circle at 50% 40%,#e4e6e8,#7d848a);transform:translateX(-50%)}
.person{top:384px;font-size:20px;color:var(--blue);transform:translateX(-50%);white-space:nowrap}

/* footer */
.site-footer{left:0;top:2290px;width:1200px;height:174px;background:var(--navy)}
.site-footer h4{position:absolute;top:14px;font-size:20px;font-weight:500;color:#fff}
.field{position:absolute;border:1px solid #6f8ba3;border-radius:6px;color:#9fb3c4;font-size:12px;padding:3px 8px}
.btn-send{left:243px;top:135px;width:74px;height:24px;border:1px solid #c8d4de;border-radius:6px;color:#fff;font-size:13px}
.social{top:133px;width:27px;height:27px;border-radius:50%;background:var(--yellow)}
.footer-menu{left:601px;top:50px;list-style:none;color:#fff;font-size:12px;line-height:17px}
.map{left:750px;top:32px;width:298px;height:128px;background:linear-gradient(135deg,#dfe4e6,#c4cfd4 50%,#a9bac4)}
.copyright{left:0;top:2464px;width:1200px;height:19px;background:var(--yellow);font-size:11px;text-align:center;line-height:19px;color:var(--ink)}
</style>
</head>
<body>

<header class="site-header abs">
  <div class="brand abs"><span class="brand-dot"></span>Byte Van</div>
  <div class="service-box abs">
    <div>
      <h4>Customer Service</h4>
      <p><svg width="14" height="18" viewBox="0 0 14 18"><rect x="1" y="1" width="12" height="16" rx="2" fill="none" stroke="#2b3540" stroke-width="2"/></svg>0127-318902</p>
    </div>
    <div>
      <h4>Service Times</h4>
      <p><svg width="14" height="18" viewBox="0 0 14 18"><path d="M2 1h10M2 17h10M3 1l8 16M11 1L3 17" stroke="#2b3540" stroke-width="2"/></svg>mon to friday</p>
    </div>
  </div>
</header>

<nav class="main-nav abs">
  <ul>
    <li style="width:78px">Home</li>
    <li style="width:115px">About us</li>
    <li style="width:103px">Store</li>
    <li style="width:110px">Gallry</li>
    <li style="width:105px">Services</li>
    <li style="width:124px">Contact us</li>
  </ul>
</nav>

<section class="hero abs">
  <div class="slider abs">
    <div class="slider-photo abs" role="img" aria-label="Open laptop being repaired with screwdriver and bit set"></div>
    <p class="slider-title abs">We repair all models &nbsp;<strong>On spott!!</strong></p>
    <span class="btn btn-read abs">read more</span>
  </div>
  <span class="arrow abs" style="left:124px"><svg width="12" height="18"><path d="M10 2L3 9l7 7" fill="none" stroke="#1a6ea3" stroke-width="3"/></svg></span>
  <span class="arrow abs" style="left:1046px"><svg width="12" height="18"><path d="M2 2l7 7-7 7" fill="none" stroke="#1a6ea3" stroke-width="3"/></svg></span>

  <div class="features abs">
    <div class="feature">
      <svg width="26" height="22" viewBox="0 0 26 22"><rect x="1" y="2" width="24" height="15" rx="2" fill="#1a6ea3"/><rect x="8" y="18" width="10" height="3" fill="#1a6ea3"/></svg>
      <h3>PC JACK REPAIR</h3>
      <p>Lorem Ipsum is simply dummy text of the printing and typesetting industry. Lorem Ipsum has been the industry's standard dummy text ever since the 1500s, when an unknown printer took a galley of type and scrambled it.</p>
    </div>
    <div class="feature">
      <svg width="26" height="22" viewBox="0 0 26 22"><circle cx="13" cy="11" r="10" fill="#1a6ea3"/><circle cx="13" cy="11" r="3" fill="#f2d935"/></svg>
      <h3>SYSTEM INSTALLATION</h3>
      <p>Lorem Ipsum is simply dummy text of the printing and typesetting industry. Lorem Ipsum has been the industry's standard dummy text ever since the 1500s, when an unknown printer took a galley of type and scrambled it.</p>
    </div>
    <div class="feature">
      <svg width="26" height="22" viewBox="0 0 26 22"><circle cx="13" cy="12" r="8" fill="#1a6ea3"/><path d="M13 4V1M5 12H2M24 12h-3" stroke="#1a6ea3" stroke-width="2"/></svg>
      <h3>VIRUS RENOVAL</h3>
      <p>Lorem Ipsum is simply dummy text of the printing and typesetting industry. Lorem Ipsum has been the industry's standard dummy text ever since the 1500s, when an unknown printer took a galley of type and scrambled it.</p>
    </div>
  </div>

  <h2 class="welcome abs">WELLCOME TO BYTE VAN</h2>

  <div class="about abs">
    <p>Byte Van are a highly professional local repair specialists based in Brookford, Westshire. We have been trading since 2004, with over 28 years experience.Here at Byte Van we offer a full range of repair, service &amp; upgrade options to suit every make and model of PC system both old &amp; new.</p>
    <p>Our specialist engineers are fully trained in all aspects of PC maintenance, and work is always carried out to the highest standards.</p>
    <p>Our specialist engineers are fully trained in all aspects of PC maintenance, and work is always carried out to the highest standards.</p>
  </div>
  <div class="van-photo abs" role="img" aria-label="Silver branded company van"></div>
</section>

<section class="brands abs">
  <span class="brand-name abs" style="left:179px">Orchard</span>
  <span class="brand-name abs" style="left:414px">Paneworks</span>
  <span class="brand-name abs" style="left:607px">Droidly</span>
  <span class="brand-name abs" style="left:800px">Hexa</span>
  <span class="brand-name abs" style="left:993px">Berrytel</span>
</section>

<section class="experts abs" role="img" aria-label="Hands repairing a phone circuit board, tinted green">
  <h2 class="experts-box abs">We are &nbsp;experts in all brands</h2>
  <span class="btn btn-market abs">View our markit</span>
  <span class="btn btn-services abs">View our services</span>
</section>

<section class="testimonials abs">
  <h2 class="testi-heading abs">CLIENT <span>TESTIMONIALS</span></h2>

  <blockquote class="quote abs" style="left:152px">
    <span class="mark" style="left:8px;top:8px">“</span>
    Lorem Ipsum is simply dummy text of the printing and typesetting industry. Lorem Ipsum has been the industry's standard dummy text ever since the 1500s.
    <span class="mark" style="right:8px;bottom:0">”</span>
  </blockquote>
  <blockquote class="quote abs" style="left:469px">
    <span class="mark" style="left:8px;top:8px">“</span>
    Lorem Ipsum is simply dummy text of the printing and typesetting industry. Lorem Ipsum has been the industry's standard dummy text ever since the 1500s.
    <span class="mark" style="right:8px;bottom:0">”</span>
  </blockquote>
  <blockquote class="quote abs" style="left:781px">
    <span class="mark" style="left:8px;top:8px">“</span>
    Lorem Ipsum is simply dummy text of the printing and typesetting industry. Lorem Ipsum has been the industry's standard dummy text ever since the 1500s.
    <span class="mark" style="right:8px;bottom:0">”</span>
  </blockquote>

  <div class="portrait abs" style="left:287px" role="img" aria-label="Portrait of client Tom harlow"></div>
  <div class="portrait abs" style="left:588px" role="img" aria-label="Portrait of client ellis moran"></div>
  <div class="portrait abs" style="left:910px" role="img" aria-label="Portrait of client Nadia vance"></div>
  <p class="person abs" style="left:287px">Tom harlow</p>
  <p class="person abs" style="left:588px">ellis moran</p>
  <p class="person abs" style="left:910px">Nadia vance</p>
</section>

<footer class="site-footer abs">
  <h4 style="left:152px">Contact us</h4>
  <div class="field" style="left:152px;top:50px;width:220px;height:22px">Name</div>
  <div class="field" style="left:152px;top:102px;width:220px;height:22px">Email</div>
  <div class="field" style="left:381px;top:42px;width:199px;height:82px">Message</div>
  <span class="btn btn-send abs">Send</span>
  <span class="social abs" style="left:407px"></span>
  <span class="social abs" style="left:456px"></span>
  <span class="social abs" style="left:505px"></span>

  <h4 style="left:601px">Menu</h4>
  <ul class="footer-menu abs">
    <li>Home</li><li>About us</li><li>Services</li><li>Store</li><li>Gallary</li><li>contact us</li>
  </ul>

  <h4 style="left:750px;top:4px">Map</h4>
  <div class="map abs" role="img" aria-label="Street map showing the shop location"></div>
</footer>

<div class="copyright abs">© 2015 Byte Van</div>

</body>
</html>
```